Building / construction Bussiness card design

I need a new design and logo for my company LWT I am a builder who can project manage or design and construct any kind of building, Residential, Commercial and industrial construction.

On the face side of the card I would like to have just the logo.

Industry/Entity Type

Construction

Contact Information for Business Card

LWT Lakeside Works Team
ABN:84 392 017 655
Carl Moretti
Licenced Builders
0471 926 054
carl@lakesideworksteam.com.au
PO Box 482 Tallowmere BC 2739

```html
<!DOCTYPE html>
<html lang="en">
<head>
<meta charset="utf-8">
<title>LWT Lakeside Works Team – Business Card</title>
<link rel="stylesheet" href="https://fonts.googleapis.com/css2?family=Open+Sans:wght@400;600;700&display=swap">
<style>
  :root {
    --brand-blue: #1f5f9e;
    --brand-blue-dark: #174a7c;
    --brand-blue-light: #4f86bd;
    --card-white: #ffffff;
    --card-shade: #eef1f4;
    --ink: #3a3f45;
    --ink-soft: #5c636b;
    --page-bg: #e6e8eb;
  }
  * { box-sizing: border-box; margin: 0; padding: 0; }
  html, body {
    width: 1200px; height: 1023px; overflow: hidden;
    background: var(--page-bg);
    font-family: "Open Sans", Arial, sans-serif;
  }
  .card-set {
    position: absolute; inset: 0;
    display: flex; align-items: center; justify-content: center; gap: 40px;
  }
  .card {
    position: relative;
    width: 520px; height: 318px;
    background: linear-gradient(160deg, var(--card-white) 0%, var(--card-shade) 100%);
    box-shadow: 0 6px 18px rgba(0,0,0,.18);
    overflow: hidden;
  }

  /* Contact side */
  .card--contact .brand-panel {
    position: absolute; left: 0; top: 0; bottom: 0; width: 190px;
    background: linear-gradient(170deg, var(--brand-blue-light) 0%, var(--brand-blue) 45%, var(--brand-blue-dark) 100%);
    display: flex; flex-direction: column; justify-content: center; align-items: center;
    color: var(--card-white);
  }
  .wordmark { color: inherit; font-weight: 600; text-align: center; line-height: 1; }
  .wordmark__initials { display: block; font-size: 64px; letter-spacing: 2px; }
  .wordmark__rule { display: block; height: 1px; background: currentColor; margin: 8px auto 6px; }
  .wordmark__name { display: block; font-size: 10px; letter-spacing: 1.5px; text-transform: uppercase; }
  .card--contact .wordmark__rule { width: 140px; }

  .card--contact .edge-stripe {
    position: absolute; left: 190px; right: 0; bottom: 0; height: 12px;
    background: var(--brand-blue);
  }
  .card--contact .edge-stripe::before {
    content: ""; position: absolute; left: 0; right: 0; top: -6px; height: 2px;
    background: var(--brand-blue);
  }
  .details {
    position: absolute; left: 214px; top: 34px; right: 20px;
    color: var(--ink);
  }
  .person__name {
    font-size: 19px; font-weight: 700; color: var(--brand-blue);
    text-transform: uppercase; letter-spacing: .5px;
  }
  .person__role { font-size: 13px; color: var(--ink-soft); margin-top: 2px; }
  .company { margin-top: 22px; font-size: 11.5px; line-height: 1.5; color: var(--ink-soft); }
  .company__name { color: var(--brand-blue); font-weight: 600; }
  .contact-list { list-style: none; margin-top: 22px; font-size: 11.5px; line-height: 1.75; color: var(--ink); }
  .contact-list li { display: flex; align-items: center; gap: 7px; }
  .contact-list .address { padding-left: 0; }
  .contact-icon {
    width: 12px; height: 12px; flex: none;
    background: var(--brand-blue); border-radius: 2px;
    display: inline-flex; align-items: center; justify-content: center;
  }
  .contact-icon svg { width: 8px; height: 8px; fill: none; stroke: var(--card-white); stroke-width: 1.6; }

  /* Logo side */
  .card--logo .website {
    position: absolute; left: 22px; top: 50%;
    transform: translate(-50%, -50%) rotate(-90deg) translateY(0);
    transform-origin: center;
    font-size: 11px; letter-spacing: 1.5px; color: var(--brand-blue);
    white-space: nowrap;
    left: 26px;
  }
  .card--logo .wordmark {
    position: absolute; left: 50%; top: 50%; transform: translate(-44%, -50%);
    color: var(--brand-blue);
  }
  .card--logo .wordmark__initials { font-size: 118px; letter-spacing: 4px; }
  .card--logo .wordmark__rule { width: 280px; margin: 12px auto 8px; }
  .card--logo .wordmark__name { font-size: 15px; letter-spacing: 2.5px; }
</style>
</head>
<body>
<main class="card-set">

  <section class="card card--contact" aria-label="Business card, contact side">
    <div class="brand-panel">
      <div class="wordmark">
        <span class="wordmark__initials">LWT</span>
        <span class="wordmark__rule"></span>
        <span class="wordmark__name">Lakeside Works Team</span>
      </div>
    </div>

    <div class="details">
      <p class="person__name">Carl Moretti</p>
      <p class="person__role">Director</p>

      <p class="company">
        <span class="company__name">Lakeside Works Team</span><br>
        ABN:84 392 017 655<br>
        Lic Builders: 0471 926 054
      </p>

      <ul class="contact-list">
        <li class="address">PO Box 482 Tallowmere BC 2739</li>
        <li>
          <span class="contact-icon"><svg viewBox="0 0 10 10"><path d="M2.5 1.5h2l.6 2-1.2.8a5 5 0 0 0 1.8 1.8l.8-1.2 2 .6v2a1 1 0 0 1-1 1A6.5 6.5 0 0 1 1.5 2.5a1 1 0 0 1 1-1z"/></svg></span>
          0471 926 054
        </li>
        <li>
          <span class="contact-icon"><svg viewBox="0 0 10 10"><rect x="1.2" y="2.2" width="7.6" height="5.6"/><path d="M1.2 2.4 5 5.5l3.8-3.1"/></svg></span>
          carl@lakesideworksteam.com.au
        </li>
        <li>
          <span class="contact-icon"><svg viewBox="0 0 10 10"><circle cx="5" cy="5" r="3.6"/><path d="M1.4 5h7.2M5 1.4c1.6 2 1.6 5.2 0 7.2M5 1.4c-1.6 2-1.6 5.2 0 7.2"/></svg></span>
          www.lakesideworksteam.com.au
        </li>
      </ul>
    </div>

    <div class="edge-stripe"></div>
  </section>

  <section class="card card--logo" aria-label="Business card, logo side">
    <p class="website">www.lakesideworksteam.com.au</p>
    <div class="wordmark">
      <span class="wordmark__initials">LWT</span>
      <span class="wordmark__rule"></span>
      <span class="wordmark__name">Lakeside Works Team</span>
    </div>
  </section>

</main>
</body>
</html>
```